Redesign of Website

We need an overhaul of our website. I've attached our current logo files. Please visit www.qelvorbis.com for our current website for information about our company. We are looking for the same type of website (information-based only) so no need for any online store, payments, interactive stuff or anything like that...basically looking for a fresh new look! Also please make sure this design will be mobile-friendly. Thanks!

```html
<!DOCTYPE html>
<html lang="en">
<head>
<meta charset="utf-8">
<title>Qelvorbis Consultants</title>
<link href="https://fonts.googleapis.com/css2?family=Open+Sans:wght@400;600;700&display=swap" rel="stylesheet">
<style>
:root{
  --navy:#0d3c84;
  --blue:#0f4c9e;
  --blue-deep:#123f86;
  --green:#8cc084;
  --green-dark:#6fa56a;
  --orange:#f7941d;
  --ink:#555;
  --muted:#888;
  --white:#fff;
}
*{margin:0;padding:0;box-sizing:border-box}
html,body{width:1200px;height:1200px;overflow:hidden;background:#fff;font-family:"Open Sans",sans-serif}
.stage{position:absolute;left:0;top:0;width:1500px;height:1500px;transform:scale(.8);transform-origin:0 0}
.abs{position:absolute}
.h2{font-weight:700;font-size:12.5px;color:var(--navy);line-height:1}
.sub{font-size:7.5px;color:var(--navy);line-height:1}
.small{font-size:4.4px;color:var(--ink);line-height:9px}
.brand{font-weight:700;color:var(--navy);font-size:15px;letter-spacing:.5px;line-height:1}
.btn{background:var(--orange);color:#fff;font-size:5px;font-weight:700;border-radius:8px;display:flex;align-items:center;justify-content:center}
.nav{left:576px;top:46px;width:350px;height:15px;background:var(--green);display:flex;align-items:center;padding-left:71px;gap:0}
.nav span{color:#fff;font-size:5.3px;font-weight:600;padding:0 4px;height:15px;line-height:15px}
.nav .active{background:var(--green-dark);padding:0 7px}
.photo{position:absolute}
.band{position:absolute;left:576px;width:350px;background:var(--blue)}
.card{position:absolute;width:92px;height:56px;background:#fff;padding:6px 7px}
.card h3{font-size:6.6px;font-weight:700;color:var(--navy);line-height:8.5px}
.card i{display:block;width:20px;height:1.6px;background:var(--blue);margin:2px 0 3px}
.card p{font-size:3.8px;color:var(--ink);line-height:7.5px}
.card b{position:absolute;right:4px;bottom:2px;font-size:10px;color:var(--green);font-weight:600}
.feat h4{font-size:7px;font-weight:700;color:var(--navy);line-height:1}
.feat p{font-size:4.3px;color:var(--ink);line-height:9px;margin-top:3px;width:100px}
.ico{position:absolute;width:25px;height:25px;border-radius:50%;background:var(--green)}
.member{position:absolute;top:980px;width:63px;text-align:center}
.member .ph{width:63px;height:52px;border:1px solid #ddd}
.member h5{font-size:4.8px;font-weight:700;color:var(--navy);margin-top:7px}
.member span{font-size:4.2px;color:var(--ink)}
.foot h6{font-size:4.6px;font-weight:700;color:var(--navy);text-decoration:underline;margin-bottom:3px}
.foot p{font-size:4.2px;color:var(--ink);line-height:8px}
.center{text-align:center}
</style>
</head>
<body>
<div class="stage">

  <!-- header -->
  <div class="abs brand" style="left:615px;top:17px">QELVORBIS</div>
  <div class="abs" style="left:615px;top:33px;font-size:4.5px;color:var(--navy);font-weight:600">CONSULTANTS</div>
  <div class="abs" style="left:812px;top:22px;font-size:7.5px;color:var(--navy)">Sign up</div>
  <div class="abs btn" style="left:842px;top:19px;width:58px;height:14px">GET STARTED</div>

  <nav class="abs nav">
    <span class="active">HOME</span><span>ABOUT US</span><span>SERVICES</span><span>TEAM MEMBERS</span><span>CONTACT</span>
  </nav>

  <!-- newsletter top -->
  <div class="abs h2" style="left:614px;top:81px">Get Latest Updates</div>
  <div class="abs" style="left:615px;top:96px;font-size:8.5px;color:#333">Provide latest ideas for your needs...</div>
  <div class="abs" style="left:615px;top:112px;font-size:5px;color:var(--muted)">Put email address</div>
  <div class="abs" style="left:614px;top:122px;width:131px;height:1px;background:#ccc"></div>
  <svg class="abs" style="left:749px;top:112px" width="12" height="12"><circle cx="6" cy="6" r="6" fill="var(--navy)"/><path d="M3 6h6M6.5 3.5 9 6 6.5 8.5" stroke="#fff" stroke-width="1.2" fill="none"/></svg>

  <!-- hero -->
  <div class="photo" role="img" aria-label="Row of red brick townhouses under a blue sky" style="left:576px;top:142px;width:350px;height:169px;background:linear-gradient(180deg,#5a6f91 0%,#8a5a45 45%,#6e3d2e 100%)"></div>
  <div class="abs" style="left:613px;top:214px;color:#fff;font-weight:700;font-size:14px;line-height:15.5px">CONSTRUCTION<br>FUNDING INSPECTION</div>
  <div class="abs" style="left:613px;top:246px;color:#fff;font-size:4.6px;line-height:7px;width:160px">It is a long established fact that a reader will be distracted by the readable content of a page when looking at its layout.</div>
  <svg class="abs" style="left:588px;top:229px" width="16" height="16"><circle cx="8" cy="8" r="8" fill="rgba(255,255,255,.35)"/><path d="M11 8H5M7.5 5.5 5 8l2.5 2.5" stroke="#fff" stroke-width="1.2" fill="none"/></svg>
  <svg class="abs" style="left:896px;top:229px" width="16" height="16"><circle cx="8" cy="8" r="8" fill="rgba(255,255,255,.35)"/><path d="M5 8h6M8.5 5.5 11 8l-2.5 2.5" stroke="#fff" stroke-width="1.2" fill="none"/></svg>

  <!-- about -->
  <div class="photo" role="img" aria-label="Businesswoman holding a tablet in a meeting" style="left:606px;top:340px;width:145px;height:148px;background:linear-gradient(135deg,#3a3f48,#9aa2ad 60%,#d8d9dc)"></div>
  <div class="abs h2" style="left:770px;top:336px">About Our Company</div>
  <div class="abs sub" style="left:771px;top:352px">Our company information</div>
  <div class="abs small" style="left:770px;top:364px;width:126px">It is a long established fact that a reader will be distracted by the readable content of a page when looking at its layout. The point of using placeholder text is that it has a more or less normal distribution of letters, as opposed to using plain repeated words, making it look like readable English. Many desktop publishing packages and web page editors now use sample text as their default model text, and a search for it will uncover many web sites still in their infancy. Please use demo text now.</div>

  <!-- services -->
  <section class="band" style="top:513px;height:204px"></section>
  <div class="abs" style="left:606px;top:533px;font-size:12.5px;font-weight:700;color:#fff">Look at Services</div>
  <div class="abs" style="left:607px;top:549px;font-size:7px;color:#fff">Qelvorbis Consultants, Inc. offers the following services...</div>
  <div class="card" style="left:607px;top:573px"><h3>Property Condition<br>Reports</h3><i></i><p>It is a long fact that a reader will be distracted content page.</p><b>01</b></div>
  <div class="card" style="left:703px;top:573px"><h3>Plan &amp; Cost<br>Reviews</h3><i></i><p>It is a long fact that a reader will be distracted content page.</p><b>02</b></div>
  <div class="card" style="left:799px;top:573px"><h3>Construction Funding<br>Inspections</h3><i></i><p>It is a long fact that a reader will be distracted content page.</p><b>03</b></div>
  <div class="card" style="left:607px;top:632px"><h3>Environmental<br>Transaction Screens</h3><i></i><p>It is a long fact that a reader will be distracted content page.</p><b>04</b></div>
  <div class="card" style="left:703px;top:632px"><h3>Phase 1 Environmental<br>Assessment</h3><i></i><p>It is a long fact that a reader will be distracted content page.</p><b>05</b></div>
  <div class="abs" style="left:807px;top:643px;color:#fff;font-size:6px;line-height:9px">Push The Button<br>To Get Expert Consultation...</div>
  <div class="abs btn" style="left:807px;top:666px;width:58px;height:14px">GET STARTED</div>

  <!-- why choose us -->
  <div class="photo" role="img" aria-label="Two women reviewing building plans, one in a hard hat" style="left:747px;top:717px;width:179px;height:211px;background:linear-gradient(160deg,#e6e2dc,#8f8a84 50%,#3b3533)"></div>
  <div class="abs h2" style="left:604px;top:737px">Why Choose Us</div>
  <div class="abs sub" style="left:605px;top:753px">Look at Our Specialities</div>
  <div class="abs small" style="left:604px;top:765px;width:128px">It is a long established fact that a reader will be distracted by the readable content of a page.</div>
  <div class="ico" style="left:604px;top:790px"></div>
  <div class="ico" style="left:604px;top:827px"></div>
  <div class="ico" style="left:604px;top:864px"></div>
  <div class="ico" style="left:604px;top:901px"></div>
  <div class="abs feat" style="left:637px;top:790px"><h4>25 YEARS EXPERIENCE</h4><p>It is a long established fact that a reader will be distracted by the readable content.</p></div>
  <div class="abs feat" style="left:637px;top:827px"><h4>EXPERT STAFF</h4><p>It is a long established fact that a reader will be distracted by the readable content.</p></div>
  <div class="abs feat" style="left:637px;top:864px"><h4>LOAN MANAGEMENT</h4><p>It is a long established fact that a reader will be distracted by the readable content.</p></div>
  <div class="abs feat" style="left:638px;top:901px"><h4>HASSLE FREE</h4><p>It is a long established fact that a reader will be distracted by the readable content.</p></div>

  <!-- team -->
  <div class="abs h2 center" style="left:576px;width:350px;top:946px">Our Expert Members</div>
  <div class="abs sub center" style="left:576px;width:350px;top:961px">Expert gives you expert advices</div>
  <svg class="abs" style="left:595px;top:997px" width="16" height="16"><circle cx="8" cy="8" r="7" fill="#fff" stroke="#aaa" stroke-width=".8"/><path d="M9 5 6 8l3 3" stroke="#888" stroke-width=".9" fill="none"/></svg>
  <svg class="abs" style="left:891px;top:997px" width="16" height="16"><circle cx="8" cy="8" r="7" fill="#fff" stroke="#aaa" stroke-width=".8"/><path d="M7 5l3 3-3 3" stroke="#888" stroke-width=".9" fill="none"/></svg>
  <div class="member" style="left:618px"><div class="ph" role="img" aria-label="Portrait of the president" style="background:linear-gradient(#f2f2f2,#c9b8a8)"></div><h5>RENN HOLLOWICK</h5><span>President</span></div>
  <div class="member" style="left:686px"><div class="ph" role="img" aria-label="Portrait of the chief financial officer" style="background:linear-gradient(#ececec,#a89a8e)"></div><h5>ODELL BRAYMAR</h5><span>Chief Financial Officer</span></div>
  <div class="member" style="left:754px"><div class="ph" role="img" aria-label="Portrait of the director of operations" style="background:linear-gradient(#cfe3f2,#8eb3cf)"></div><h5>TAVI ORLENKO</h5><span>Director of Operations</span></div>
  <div class="member" style="left:822px"><div class="ph" role="img" aria-label="Portrait of the product distribution manager" style="background:linear-gradient(#f4f1ec,#c7a48a)"></div><h5>MIRA CASTLUND</h5><span>Product Distribution Manager</span></div>

  <!-- testimonials -->
  <section class="band" role="img" aria-label="Blue tinted office scene behind testimonials" style="top:1070px;height:194px;background:linear-gradient(180deg,#3f6fae,#1f559f)"></section>
  <div class="abs center" style="left:576px;width:350px;top:1085px;color:#fff;font-size:12.5px;font-weight:700">What Our Clients Say</div>
  <div class="abs center" style="left:576px;width:350px;top:1101px;color:#fff;font-size:7px">Expert gives you expert advices</div>
  <div class="abs" style="left:614px;top:1121px;width:273px;height:112px;background:#fff"></div>
  <div class="abs" role="img" aria-label="Client portrait" style="left:727px;top:1130px;width:38px;height:38px;border-radius:50%;background:linear-gradient(#e9d2c0,#a97e63)"></div>
  <div class="abs center" style="left:614px;width:273px;top:1172px;font-size:8px;font-weight:700;color:var(--navy)">Jory Vantell</div>
  <div class="abs center" style="left:614px;width:273px;top:1182px;font-size:6px;color:#333">President Of Company</div>
  <div class="abs center small" style="left:655px;width:191px;top:1193px">It is a long established fact that a reader will be distracted by the readable content of a page.It is a long established fact that a reader will be distracted by the content.</div>
  <svg class="abs" style="left:733px;top:1214px" width="28" height="6"><circle cx="3" cy="3" r="2" fill="#ddd"/><circle cx="10" cy="3" r="2" fill="#bbb"/><circle cx="17" cy="3" r="2" fill="#ddd"/><circle cx="24" cy="3" r="2" fill="#ddd"/></svg>
  <svg class="abs" style="left:604px;top:1171px" width="18" height="18"><circle cx="9" cy="9" r="8.5" fill="#24205e"/><path d="M12.5 9h-7M8 6.5 5.5 9 8 11.5" stroke="#fff" stroke-width="1.2" fill="none"/></svg>
  <svg class="abs" style="left:877px;top:1171px" width="18" height="18"><circle cx="9" cy="9" r="8.5" fill="#24205e"/><path d="M5.5 9h7M10 6.5 12.5 9 10 11.5" stroke="#fff" stroke-width="1.2" fill="none"/></svg>

  <!-- newsletter bottom -->
  <section class="band" style="top:1296px;height:105px"></section>
  <div class="abs" style="left:619px;top:1326px;color:#fff;font-size:12.5px;font-weight:700">Get Latest Updates</div>
  <div class="abs" style="left:620px;top:1342px;color:#fff;font-size:8.5px">Provide latest ideas for your needs...</div>
  <div class="abs" style="left:620px;top:1358px;color:#fff;font-size:5px">Put email address</div>
  <div class="abs" style="left:620px;top:1368px;width:128px;height:1px;background:rgba(255,255,255,.7)"></div>
  <svg class="abs" style="left:754px;top:1358px" width="12" height="12"><circle cx="6" cy="6" r="6" fill="#fff"/><path d="M3 6h6M6.5 3.5 9 6 6.5 8.5" stroke="var(--navy)" stroke-width="1.2" fill="none"/></svg>

  <!-- footer -->
  <footer>
    <div class="abs brand" style="left:620px;top:1430px;font-size:12px">QELVORBIS</div>
    <div class="abs" style="left:620px;top:1444px;font-size:4.5px;color:var(--navy);font-weight:600">CONSULTANTS</div>
    <div class="abs foot" style="left:703px;top:1413px"><h6>SITELINK</h6><p>Home<br>About us<br>Services<br>Members<br>Contact us</p></div>
    <div class="abs foot" style="left:745px;top:1413px"><h6>WHY CHOOSE US</h6><p>Hassle free<br>Loan management<br>Expert advice</p></div>
    <div class="abs foot" style="left:794px;top:1413px"><h6>COMPANY RULES</h6><p>Rules &amp; regulations<br>Privacy policy<br>Terms conditions<br>Help</p></div>
    <div class="abs foot" style="left:848px;top:1413px"><h6>CONTACT US</h6>
      <p style="padding-left:7px">555-014-2270<br>48 Larkmoor Rd,<br>Suite 12 Fenwick Hollow,<br>ST 00000</p></div>
    <svg class="abs" style="left:848px;top:1422px" width="6" height="20"><path d="M1 1.5c0 2 2 4 4 4l.6-1.2-1.2-.8-.6.6C3 3.7 2.3 3 2 2.2l.6-.6-.8-1.2z" fill="var(--navy)"/><path d="M3 10a2 2 0 0 1 2 2c0 1.5-2 3.5-2 3.5S1 13.5 1 12a2 2 0 0 1 2-2z" fill="none" stroke="var(--navy)" stroke-width=".7"/></svg>
    <svg class="abs" style="left:851px;top:1457px" width="28" height="8"><circle cx="4" cy="4" r="3.6" fill="var(--navy)"/><circle cx="13" cy="4" r="3.6" fill="var(--navy)"/><circle cx="22" cy="4" r="3.6" fill="var(--navy)"/></svg>
    <div class="abs" style="left:576px;top:1473px;width:350px;height:1px;background:#ccc"></div>
    <div class="abs center" style="left:576px;width:336px;top:1480px;font-size:4px;color:var(--muted)">© 2003-2019 qelvorbis.com, Inc. All rights reserved.</div>
  </footer>

</div>
</body>
</html>
```